VOSKE - New website for high-quality knives, aprons, chopping boards and caps for Grillers

We would like to develop a new website for our brand-new outdoor cooking brand VOSKE. VOSKE is a brand by grillers for grillers. Therefore the griller will always be in the centre of everything that we do. We want to appear as a cool, robust brand without being too stereotypical (like any other BBQ brands (so not too much black, red, flames)). We're very international and that should also come back in the design.

Main colour will be the yellow supported by red white and black. However, we're also open to other colours

VOSKE will be sold in-store but we want to provide more information to our clients via the website. This will be done through detailed descriptions but also blogs and downloads. We will work together with influencers to share recipes in our Pavane (magazine) and on our blog page.

Website needs to be responsive (web+mobile) and our own team should be able to easily add new content to the website.

Target Market(s)

International grillers or home chefs

Industry/Entity Type

BBQ and outdoor cooking

Coding

Coded - Design and coding required

Other font styles liked:
• Allan & Cambria

Colors

Designer to choose colors to be used in the design.

Requirements
Must have
• home, products (not shop), blog, contact, socials, downloads (for Pavane).
Nice to have
• instagram grid with #voske
Should not have
• too stereotypical BBQ website (red, flames, black)

```html
<!DOCTYPE html>
<html lang="nl">
<head>
<meta charset="utf-8">
<title>VOSKE – Online Strategie</title>
<link href="https://fonts.googleapis.com/css2?family=Nunito:wght@700;800;900&family=Open+Sans:wdth,wght@75,300;75,400;75,600;75,700&family=Oswald:wght@300;400;500&display=swap" rel="stylesheet">
<style>
:root{
  --yellow:#f7c21d;
  --yellow-deep:#f2b705;
  --slate:#3e4a5b;
  --ink:#1d1d1d;
  --text:#3a3a3a;
  --soft:#f5f5f5;
  --line:#e2e2e2;
  --footer:#262626;
  --white:#ffffff;
}
*{box-sizing:border-box;margin:0;padding:0}
html,body{width:1200px;height:5000px;overflow:hidden;background:var(--white)}
body{position:relative;font-family:"Open Sans",Arial,sans-serif;font-stretch:75%;color:var(--text)}
.abs{position:absolute}
.heading{font-family:"Nunito",Arial,sans-serif;font-weight:800;color:var(--ink);letter-spacing:1px}
.tag{position:absolute;background:var(--yellow);font-family:"Oswald",Arial,sans-serif;font-weight:300;color:#3a2a00;letter-spacing:1px;line-height:1}

/* hero */
.hero{position:absolute;left:0;top:0;width:1200px;height:643px;
  background:radial-gradient(ellipse at 35% 25%,#6a4a34 0%,#2b1d16 35%,transparent 60%),
  linear-gradient(180deg,#1a1411 0%,#2a1c15 40%,#5c1f0d 70%,#c2481a 88%,#3a1a0e 100%)}
.brand-mark{position:absolute;left:46px;top:21px;width:128px;height:128px;border-radius:50%;background:var(--yellow);
  display:flex;align-items:center;justify-content:center;font-family:"Open Sans",sans-serif;font-stretch:75%;font-weight:700;font-size:34px;color:var(--white);letter-spacing:1px}
.nav{position:absolute;top:76px;right:32px;display:flex;gap:34px;font-size:15px;color:var(--white)}
.search{position:absolute;right:30px;top:24px;display:flex;align-items:center;gap:8px;font-size:13px;font-style:italic;color:#ddd}
.search span{border-bottom:1px solid #bbb;padding:0 4px 1px;width:110px}
.hero-kicker{position:absolute;right:49px;top:196px;font-family:"Oswald",sans-serif;font-weight:300;font-size:27px;letter-spacing:2px;color:var(--yellow)}
.hero-title{position:absolute;right:32px;top:272px;text-align:right;font-family:"Nunito",sans-serif;font-weight:800;font-size:106px;line-height:112px;color:var(--white)}

/* about */
.about-title{left:0;width:1118px;text-align:center;top:655px;font-size:58px}
.about-text{left:95px;width:930px;top:782px;text-align:center;font-size:23px;line-height:30px}

/* products band */
.products{position:absolute;left:0;top:867px;width:1200px;height:561px;background:var(--slate)}
.products-photo{position:absolute;right:0;top:0;width:620px;height:561px;
  background:linear-gradient(115deg,var(--slate) 0%,#2a2f36 25%,#3a3a3a 45%,#8a5a3a 60%,#2c2c2c 75%,#4b4b4b 100%)}
.products h2{position:absolute;left:82px;top:78px;font-size:56px;color:var(--white)}
.products .tag{left:85px;top:178px;width:227px;height:54px;padding:14px 0 0 28px;font-size:29px}
.products p{position:absolute;left:111px;top:255px;width:520px;font-size:23px;line-height:33px;color:#e8e8e8}

/* product cards */
.product-figure{position:absolute;top:1401px;width:260px;height:415px;background:linear-gradient(180deg,#7a7a7a 0%,#2a2a2a 45%,#111 100%);border-radius:40px 40px 14px 14px;opacity:.9}
.product-yellow{position:absolute;left:437px;top:1455px;width:314px;height:418px;background:var(--yellow)}
.view-details{position:absolute;left:516px;top:1843px;width:155px;height:32px;background:#1d1d1d;color:var(--white);font-size:21px;text-align:center;line-height:32px;border-radius:4px 4px 0 0}
.corner{position:absolute;width:94px;height:94px;border:8px solid var(--line)}
.product-tag{position:absolute;top:1904px;height:36px;padding:5px 20px;background:var(--yellow);font-family:"Open Sans",sans-serif;font-stretch:75%;font-weight:700;font-size:25px;color:#2a1f00;line-height:26px}
.product-text{position:absolute;top:1950px;width:260px;font-size:23px;line-height:30px;color:#333}
.btn-outline{position:absolute;left:499px;top:2066px;width:202px;height:58px;border:3px solid var(--yellow);font-family:"Oswald",sans-serif;font-weight:300;font-size:24px;color:#555;text-align:center;line-height:52px;letter-spacing:1px}

/* socials */
.socials{position:absolute;left:0;top:2138px;width:1200px;height:429px;background:var(--soft)}
.socials h2{position:absolute;left:82px;top:16px;font-size:56px}
.socials .tag{left:85px;top:106px;width:312px;height:56px;padding:14px 0 0 28px;font-size:30px}
.label{position:absolute;left:111px;font-weight:700;font-size:22px;color:var(--yellow-deep)}
.statement{position:absolute;left:111px;width:930px;font-size:23px;line-height:33px;color:#333}

/* instagram grid */
.insta{position:absolute;left:0;top:2567px;width:1200px;height:832px;
  background:linear-gradient(90deg,#e9ece4 0%,#8c9a78 8%,#3b3b3b 14%,#8a8a8a 30%,#2c2c2c 45%,#5a6a46 60%,#3c5a3a 72%,#4c6d90 86%,#7b8da4 100%)}
.insta svg{position:absolute;left:0;top:0}

/* blog */
.blog-title{left:82px;top:3413px;font-size:56px}
.blog .tag{left:85px;top:3490px;width:330px;height:56px;padding:14px 0 0 28px;font-size:30px}
.blog-card{position:absolute;top:3570px;width:312px;height:333px;background:#ececec}
.blog-card .photo{height:170px;background:linear-gradient(160deg,#4a3a30 0%,#1f1a17 50%,#b06a2a 100%)}
.blog-card p{padding:12px 18px 0;font-size:23px;line-height:30px;color:#444}
.blog-card .more{position:absolute;right:18px;bottom:14px;font-size:15px;color:#333;display:flex;align-items:center;gap:8px}

/* downloads */
.downloads{position:absolute;left:0;top:3936px;width:1200px;height:159px;background:linear-gradient(90deg,var(--yellow) 0%,#f9ca2d 50%,var(--yellow) 100%)}
.downloads h2{position:absolute;left:315px;top:42px;font-size:58px;color:#1d1d1d}
.downloads svg{position:absolute;left:762px;top:14px}

/* contact */
.contact-title{left:0;width:1200px;text-align:center;top:4115px;font-size:58px}
.contact-text{left:140px;width:920px;top:4203px;text-align:center;font-size:22px;line-height:29px}
.field{position:absolute;background:var(--white);border-radius:14px;box-shadow:0 3px 14px rgba(0,0,0,.12);font-size:27px;color:#999;padding:18px 38px;font-weight:300}
.submit{position:absolute;left:501px;top:4738px;width:207px;height:77px;background:var(--yellow);border-radius:14px;font-family:"Nunito",sans-serif;font-weight:800;font-size:38px;color:#1d1d1d;text-align:center;line-height:77px}

/* footer */
.footer{position:absolute;left:0;top:4864px;width:1200px;height:136px;background:var(--footer)}
.footer-badge{position:absolute;right:0;top:4840px;width:294px;height:33px;background:var(--yellow);font-size:19px;color:#1d1d1d;text-align:center;line-height:33px;letter-spacing:1px}
.footer .brand-mark{left:58px;top:20px;width:90px;height:90px;font-size:22px}
.footer-slogan{position:absolute;left:182px;top:28px;font-family:"Oswald",sans-serif;font-size:24px;line-height:34px;letter-spacing:1px;color:var(--white);font-weight:300}
.footer-slogan b{color:var(--yellow);font-weight:500}
.social-dot{position:absolute;top:53px;width:46px;height:46px;border:2px solid var(--yellow);border-radius:50%}
.footer-address{position:absolute;left:940px;top:38px;width:230px;text-align:center;font-size:19px;line-height:25px;color:var(--white)}
.footer-address b{color:var(--yellow);font-weight:400}
</style>
</head>
<body>

<!-- hero -->
<header class="hero" role="img" aria-label="Close-up photo of a steak on a glowing charcoal grill">
  <div class="brand-mark">VOSKE</div>
  <div class="search"><span>I'm looking for...</span>
    <svg width="20" height="20" viewBox="0 0 20 20"><circle cx="8" cy="8" r="6" fill="none" stroke="#f7c21d" stroke-width="2"/><line x1="12.5" y1="12.5" x2="18" y2="18" stroke="#f7c21d" stroke-width="2"/></svg>
  </div>
  <nav class="nav">
    <span>Het verhaal</span><span>USP</span><span>De Missie &amp; Visie</span><span>The VOSKE Brand</span><span>Online Presence</span><span>Social Guidelines</span><span>The Roll Out</span>
  </nav>
  <div class="hero-kicker">VOSKE | FOR VOSKES BY VOSKES</div>
  <h1 class="hero-title">Ontline<br>Strategie</h1>
</header>

<!-- about -->
<h2 class="abs heading about-title">About The VOSKE</h2>
<div class="tag" style="left:513px;top:732px;width:174px;height:38px;padding:8px 0 0;text-align:center;font-family:'Open Sans',sans-serif;font-stretch:75%;font-weight:700;font-size:24px;">HET VERHAAL</div>
<p class="abs about-text">VOSKE is een merk ontwikkeld door grillers voor grillers. Hoge kwaliteit messen, apparel en petten voor verschillende doelgroepen. De griller staat altijd centraal.</p>

<!-- products -->
<section class="products">
  <div class="products-photo" role="img" aria-label="Photo of hands holding a leather knife roll with knives"></div>
  <h2 class="heading">Products</h2>
  <div class="tag">HET VERHAAL</div>
  <p>Lorem Ipsum is simply dummy text of the printing and typesetting industry. Lorem Ipsum has been the industry's standard dummy text ever since the 1500s, when an unknown printer took a galley of type and scrambled it to make a type specimen book. It has survived not only five centuries, but also the leap into electronic typesetting,</p>
</section>

<div class="corner" style="left:53px;top:1455px;border-right:none;border-bottom:none"></div>
<div class="corner" style="left:271px;top:1757px;border-left:none;border-top:none"></div>
<div class="corner" style="left:1042px;top:1455px;border-left:none;border-bottom:none"></div>
<div class="corner" style="left:823px;top:1779px;border-right:none;border-top:none"></div>
<div class="product-yellow"></div>

<div class="product-figure" style="left:105px" role="img" aria-label="Product photo of a griller in apron and cap beside a black barrel grill"></div>
<div class="product-figure" style="left:462px" role="img" aria-label="Product photo of a griller in apron and cap beside a black barrel grill"></div>
<div class="product-figure" style="left:850px" role="img" aria-label="Product photo of a griller in apron and cap beside a black barrel grill"></div>
<div class="view-details">View Details</div>

<div class="product-tag" style="left:58px">FIRE UNION</div>
<p class="product-text" style="left:63px">Een website in lijn met waar VOSKE voor staat (dus voor de VOSKE)</p>
<div class="product-tag" style="left:442px">FIRE UNION</div>
<p class="product-text" style="left:448px">Een website in lijn met waar VOSKE voor staat (dus voor de VOSKE)</p>
<div class="product-tag" style="left:828px">FIRE UNION</div>
<p class="product-text" style="left:833px">Een website in lijn met waar VOSKE voor staat (dus voor de VOSKE)</p>

<div class="btn-outline">VIEW ALL VOSKE</div>

<!-- socials -->
<section class="socials">
  <h2 class="heading">Socials</h2>
  <div class="tag">WHAT WE AIM TO BE</div>
  <div class="label" style="top:180px">Missie:</div>
  <p class="statement" style="top:214px">De hoogste kwaliteit premium cooking supplies waar grillers, thuischefs en bourgondiërs zich verbonden mee voelen.</p>
  <div class="label" style="top:294px">Visie:</div>
  <p class="statement" style="top:335px">Dit wordt VOSKE door altijd de griller centraal te laten staan in alles wat zij doen (online en offline).</p>
</section>

<!-- instagram grid -->
<section class="insta" role="img" aria-label="Social photo grid for #voske: herbs and lemon, hands cutting meat, friends dining in a garden">
  <svg width="1200" height="832" viewBox="0 0 1200 832">
    <rect x="534" y="26" width="97" height="86" fill="#f7c21d"/>
    <rect x="446" y="640" width="286" height="150" fill="#f7c21d"/>
    <g stroke="#ffffff" stroke-width="7">
      <line x1="74" y1="0" x2="74" y2="832"/>
      <line x1="291" y1="0" x2="291" y2="832"/>
      <line x1="442" y1="0" x2="442" y2="832"/>
      <line x1="592" y1="0" x2="592" y2="832"/>
      <line x1="733" y1="0" x2="733" y2="832"/>
      <line x1="883" y1="0" x2="883" y2="832"/>
      <line x1="1042" y1="0" x2="1042" y2="832"/>
      <line x1="0" y1="40" x2="1200" y2="40"/>
      <line x1="0" y1="200" x2="1200" y2="200"/>
      <line x1="0" y1="340" x2="1200" y2="340"/>
      <line x1="0" y1="485" x2="1200" y2="485"/>
      <line x1="0" y1="636" x2="1200" y2="636"/>
      <line x1="0" y1="790" x2="1200" y2="790"/>
    </g>
  </svg>
</section>

<!-- blog -->
<section class="blog">
  <h2 class="abs heading blog-title">Blog</h2>
  <div class="tag">STOER MAAR VERFIJND</div>
  <article class="blog-card" style="left:103px">
    <div class="photo" role="img" aria-label="Photo of a plate with grilled shrimp"></div>
    <p>Alle producten in de range zijn stoer, maar wel van hoge kwaliteit en verfijnde.</p>
    <div class="more">Read More <svg width="22" height="12" viewBox="0 0 22 12"><path d="M0 6h20M15 1l5 5-5 5" fill="none" stroke="#333" stroke-width="1.5"/></svg></div>
  </article>
  <article class="blog-card" style="left:462px">
    <div class="photo" role="img" aria-label="Photo of meat on a barbecue grill"></div>
    <p>Alle producten in de range zijn stoer, maar wel van hoge kwaliteit en verfijnde.</p>
    <div class="more">Read More <svg width="22" height="12" viewBox="0 0 22 12"><path d="M0 6h20M15 1l5 5-5 5" fill="none" stroke="#333" stroke-width="1.5"/></svg></div>
  </article>
  <article class="blog-card" style="left:823px">
    <div class="photo" role="img" aria-label="Photo of steaks being turned with tongs on a grill"></div>
    <p>Alle producten in de range zijn stoer, maar wel van hoge kwaliteit en verfijnde.</p>
    <div class="more">Read More <svg width="22" height="12" viewBox="0 0 22 12"><path d="M0 6h20M15 1l5 5-5 5" fill="none" stroke="#333" stroke-width="1.5"/></svg></div>
  </article>
</section>

<!-- downloads -->
<section class="downloads">
  <h2 class="heading">Downloads</h2>
  <svg width="130" height="130" viewBox="0 0 130 130" aria-label="PDF download">
    <path d="M30 10h60l26 26v86H30z" fill="#ffffff" stroke="#cfcfcf" stroke-width="2"/>
    <path d="M90 10v26h26" fill="#e9e9e9" stroke="#cfcfcf" stroke-width="2"/>
    <rect x="6" y="14" width="70" height="30" fill="#c8202a"/>
    <text x="41" y="37" text-anchor="middle" font-family="Open Sans, sans-serif" font-weight="700" font-size="22" fill="#ffffff">PDF</text>
    <path d="M30 50h22v26h16l-27 30-27-30h16z" fill="#c8202a"/>
  </svg>
</section>

<!-- contact -->
<h2 class="abs heading contact-title">Let's Talk. Send us anything</h2>
<p class="abs contact-text">Lorem Ipsum is simply dummy text of the printing and typesetting industry. Lorem Ipsum has been the industry's standard dummy text ever since the 1500s,</p>
<div class="field" style="left:177px;top:4311px;width:415px;height:75px">Frist Name</div>
<div class="field" style="left:625px;top:4311px;width:417px;height:75px">Last Name</div>
<div class="field" style="left:177px;top:4402px;width:865px;height:78px">Email Address</div>
<div class="field" style="left:177px;top:4491px;width:865px;height:78px">Subject</div>
<div class="field" style="left:177px;top:4586px;width:865px;height:128px">Type Your Message</div>
<div class="submit">Submit</div>

<!-- footer -->
<div class="footer-badge">VOSKE ONLINE STRATEGIE</div>
<footer class="footer">
  <div class="brand-mark">VOSKE</div>
  <div class="footer-slogan"><b>LET'S GO!</b><br>VOSKE BY GRILLERS FOR GRILLERS</div>
  <div class="social-dot" style="left:643px"></div>
  <div class="social-dot" style="left:705px"></div>
  <div class="social-dot" style="left:765px"></div>
  <div class="footer-address"><b>Address</b><br>Online: - website zsm live<br>- socials beginnen</div>
</footer>

</body>
</html>
```